Tern Hollow Print and Mailing Services

We are looking for a website layout design for a direct print and mailing company which prints graphics, post cards, letters, does mailing and more.

Please see attached logo, as it will be used to match color scheme of website.

Current website:
www.ternhollowprintmail.com

Websites we like:
https://quillbaypressworks.com

Target Market(s)

Businesses / Media

Number of Pages Required

3 page

Font styles to use
Sans Serif

Requirements
Must have
• Color scheme to match logo

```html
<!DOCTYPE html>
<html lang="en">
<head>
<meta charset="utf-8">
<title>Tern Hollow Print and Mailing Services</title>
<link rel="stylesheet" href="https://fonts.googleapis.com/css2?family=Montserrat:wght@400;500;600;700&display=swap">
<style>
:root{
  --red:#e0193f;
  --pink:#e4007c;
  --navy:#232833;
  --ink:#2a2d34;
  --text:#3c3f46;
  --muted:#8a8e96;
  --line:#c9ccd2;
  --white:#ffffff;
  --footer:#2b2f3a;
}
*{box-sizing:border-box;margin:0;padding:0}
html,body{width:1200px;height:3285px;overflow:hidden}
body{font-family:"Montserrat",sans-serif;color:var(--text);background:var(--white);position:relative}
section,header,footer{position:absolute;left:0;width:1200px}

/* header */
.site-header{top:0;height:149px;border-bottom:1px solid #e6e6ea}
.brand{position:absolute;left:88px;top:34px;display:flex;align-items:center;gap:12px}
.brand-dot{width:22px;height:22px;border-radius:50%;background:var(--red)}
.brand-name{font-size:26px;font-weight:700;color:var(--navy)}
.client-area{position:absolute;left:872px;top:27px;font-size:16px;font-weight:500;color:var(--navy)}
.sign-in{display:inline-flex;align-items:center;gap:8px;margin-top:8px;border:1px solid var(--line);padding:4px 14px;font-size:13px;font-weight:500;color:var(--navy)}
.main-nav{position:absolute;left:92px;top:118px;display:flex;gap:34px;font-size:13px;font-weight:600;color:var(--red);text-transform:uppercase}

/* hero */
.hero{top:149px;height:468px;background:linear-gradient(100deg,#3c3c40 0%,#6b6f76 14%,#d9c23a 24%,#e47a2a 34%,#d23a6a 44%,#7a3fb0 54%,#3b8de0 64%,#f2f2f2 74%,#e0d6cc 86%,#f1efec 100%)}
.hero-box{position:absolute;left:278px;top:92px;width:635px;height:267px;border:2px solid rgba(255,255,255,.85);background:rgba(255,255,255,.55);display:flex;flex-direction:column;justify-content:center;align-items:center;text-align:center;line-height:1.3}
.hero-title{font-size:48px;font-weight:500;letter-spacing:3px;color:var(--navy)}
.hero-sub{font-size:48px;font-weight:700;letter-spacing:3px;color:var(--red)}

/* services band */
.services{top:617px;height:160px;background:#f4f4f6;border-bottom:4px solid var(--pink)}
.services-label{position:absolute;left:0;top:0;width:412px;height:156px;background:var(--navy);color:var(--white);font-size:38px;font-weight:500;line-height:1.15;padding:36px 0 0 86px}
.service-card{position:absolute;top:0;height:156px;background:var(--white);border-right:1px solid #e2e2e6;display:flex;flex-direction:column;align-items:center;justify-content:center;text-align:center;font-size:13px;font-weight:500;color:var(--navy);line-height:1.4;gap:10px}
.view-more{position:absolute;left:959px;top:0;width:241px;height:156px;background:var(--white);color:var(--red);font-size:28px;font-weight:500;line-height:1.1;display:flex;align-items:center;padding-left:46px}

/* about */
.about{top:781px;height:419px;background:linear-gradient(160deg,#ffffff 55%,#eef3f8 100%)}
.section-title{font-size:32px;font-weight:500;color:var(--ink);letter-spacing:1px}
.about .section-title{position:absolute;left:88px;top:50px}
.about-copy{position:absolute;left:88px;top:112px;width:570px;font-size:12.5px;line-height:22.8px}
.btn{display:flex;align-items:center;justify-content:center;gap:10px;border:1px solid var(--line);background:var(--white);font-size:13px;font-weight:500;color:var(--navy);text-transform:uppercase}
.about .btn{position:absolute;left:88px;top:306px;width:218px;height:46px}
.about-art{position:absolute;left:722px;top:46px;width:372px;height:300px;border-radius:50%;background:radial-gradient(circle at 40% 40%,#ffffff,#d8dde6 55%,#8fa0b8 100%)}

/* news */
.news{top:1200px;height:530px;border-top:1px solid #e4e4e8}
.news .section-title{position:absolute;width:100%;text-align:center;top:50px}
.news-item{position:absolute;width:476px;height:123px}
.news-thumb{position:absolute;left:0;top:0;width:174px;height:123px}
.news-date{position:absolute;left:174px;top:0;width:164px;height:20px;background:var(--red);color:var(--white);font-size:12px;font-weight:600;padding:2px 0 0 30px}
.news-text{position:absolute;left:204px;top:28px;width:272px;font-size:12.5px;line-height:1.8}
.news .btn{position:absolute;left:490px;top:420px;width:220px;height:48px}

/* testimonial */
.testimonial{top:1730px;height:486px;background:radial-gradient(ellipse at center,#2e323a 0%,#15171c 100%);color:var(--white);text-align:center}
.testimonial .section-title{color:var(--white);margin-top:52px}
.quote-box{margin:28px auto 0;width:48px;height:56px;border:2px solid var(--white);display:flex;align-items:center;justify-content:center}
.quote-text{width:840px;margin:38px auto 0;font-size:13px;line-height:1.8}
.quote-author{margin-top:38px;font-size:13px;font-weight:600;letter-spacing:1px}
.quote-author span{font-weight:400;color:#c4c7cd}
.dots{display:flex;gap:8px;justify-content:center;margin-top:56px}
.dot{width:9px;height:9px;border:1px solid var(--white)}
.dot.active{background:#f07021;border-color:#f07021}

/* contact */
.contact{top:2216px;height:521px;background:linear-gradient(135deg,#ffffff 0%,#f2f4f8 50%,#ffffff 100%);border-bottom:1px solid #e0e0e4}
.contact .section-title{position:absolute;width:100%;text-align:center;top:50px}
.contact-form{position:absolute;left:239px;top:110px;width:722px}
.customer-q{font-size:12px;font-weight:500;color:var(--navy);margin-bottom:10px;display:flex;gap:8px;align-items:center}
.radio{display:inline-flex;align-items:center;gap:4px}
.radio i{width:8px;height:8px;border-radius:50%;border:1px solid var(--muted);display:inline-block}
.radio i.on{background:var(--muted)}
.field-row{display:flex;gap:16px;margin-bottom:15px}
.field{flex:1;height:35px;border:1px solid #b9bdc5;background:var(--white);font-size:12.5px;font-weight:500;color:var(--navy);padding:7px 10px;text-transform:uppercase}
.field.tall{height:99px}
.contact .btn{position:absolute;left:490px;top:410px;width:220px;height:47px}

/* info */
.info{top:2737px;height:191px;background:var(--white)}
.info-item{position:absolute;top:60px;display:flex;gap:28px}
.info-item h3{font-size:22px;font-weight:500;color:var(--ink);margin-bottom:8px}
.info-item p{font-size:13.5px;font-weight:500;line-height:1.6;color:var(--navy)}

/* map */
.map{top:2928px;height:296px;background:linear-gradient(120deg,#dfeecf 0%,#eeeeec 22%,#f3f2ef 60%,#e7e9ec 100%)}

.site-footer{top:3224px;height:61px;background:var(--footer);color:var(--white);font-size:13px;display:flex;align-items:center;justify-content:center}
</style>
</head>
<body>

<header class="site-header">
  <div class="brand"><span class="brand-dot"></span><span class="brand-name">Tern Hollow</span></div>
  <div class="client-area">Current Client &amp; New Client<br>
    <span class="sign-in">SIGN IN
      <svg width="10" height="10" viewBox="0 0 10 10"><path d="M1 5h7M5 2l3 3-3 3" stroke="#e0193f" stroke-width="1.8" fill="none"/></svg>
    </span>
  </div>
  <nav class="main-nav">
    <span>Home</span><span>Services &amp; Print</span><span>Products Quotes &amp; Custom Orders</span><span>My Invoice Account</span><span>News</span><span>FAQ</span><span>About Us</span><span>Contact Us</span>
  </nav>
</header>

<section class="hero" role="img" aria-label="Hand holding an open colour swatch fan">
  <div class="hero-box">
    <div class="hero-title">MASTERS OF VIBRANT<br>COLOR</div>
    <div class="hero-sub">DIGITAL PRINT AND<br>MARKETING</div>
  </div>
</section>

<section class="services">
  <div class="services-label">OUR SERVICES<br>&amp; PRODUCTS</div>
  <div class="service-card" style="left:412px;width:153px">
    <svg width="44" height="34" viewBox="0 0 44 34"><rect x="2" y="6" width="26" height="18" fill="#1f5f8b"/><path d="M28 12h8l6 7v5H28z" fill="#1f5f8b"/><circle cx="10" cy="27" r="4" fill="#232833"/><circle cx="34" cy="27" r="4" fill="#232833"/></svg>
    <span>FULFILLMENT<br>SERVICES</span>
  </div>
  <div class="service-card" style="left:565px;width:110px">
    <svg width="36" height="36" viewBox="0 0 36 36"><rect x="4" y="12" width="28" height="16" fill="#18a89a"/><rect x="9" y="4" width="18" height="10" fill="none" stroke="#18a89a" stroke-width="2"/><rect x="9" y="24" width="18" height="8" fill="#ffffff" stroke="#18a89a" stroke-width="2"/></svg>
    <span>MAIL<br>SHORTING</span>
  </div>
  <div class="service-card" style="left:675px;width:142px">
    <svg width="32" height="36" viewBox="0 0 32 36"><rect x="6" y="4" width="20" height="28" rx="3" fill="#f2a9c4"/><rect x="10" y="10" width="12" height="2" fill="#fff"/><rect x="10" y="15" width="12" height="2" fill="#fff"/></svg>
    <span>LETTERSHOP<br>SERVICES</span>
  </div>
  <div class="service-card" style="left:817px;width:142px">
    <svg width="36" height="36" viewBox="0 0 36 36"><rect x="4" y="6" width="26" height="24" fill="none" stroke="#3fb54a" stroke-width="2.5"/><path d="M10 22l6-6 4 4 10-12" stroke="#3fb54a" stroke-width="2.5" fill="none"/></svg>
    <span>GRAPHIC DESIGN<br>SERVICES</span>
  </div>
  <div class="view-more">View<br>More</div>
</section>

<section class="about">
  <h2 class="section-title">ABOUT US</h2>
  <p class="about-copy">Lorem Ipsum is simply dummy text of the printing and typesetting industry. Lorem Ipsum has been the industry's standard dummy text ever since the 1500s, when an unknown printer took a galley of type and scrambled it to make a type specimen book. It has survived not only five centuries, but also the 1960s with the release of Velmark sheets co. Lorem Ipsum is simply dummy text of the printing and typesetting industry. Lorem Ipsum has been the industry's standard dummy text ever since the 1500s, when an unknown printer took a galley of type and scrambled.</p>
  <div class="btn">READ MORE <svg width="10" height="10" viewBox="0 0 10 10"><path d="M1 5h7M5 2l3 3-3 3" stroke="#e0193f" stroke-width="1.8" fill="none"/></svg></div>
  <div class="about-art" role="img" aria-label="Round collage of design desk, colour swatches and type samples"></div>
</section>

<section class="news">
  <h2 class="section-title">NEWS</h2>
  <article class="news-item" style="left:88px;top:118px">
    <div class="news-thumb" role="img" aria-label="Colour print samples" style="background:linear-gradient(135deg,#e9c23a,#6aa84f,#2f7fc1)"></div>
    <div class="news-date">21 MAY 2018</div>
    <p class="news-text">Lorem Ipsum is simply dummy text of the printing and typesetting industry. Lorem Ipsum has been the industry's standard dummy text ever since the 1500s.</p>
  </article>
  <article class="news-item" style="left:624px;top:118px">
    <div class="news-thumb" role="img" aria-label="Customer relationship sketch notes" style="background:linear-gradient(135deg,#e8dcc0,#c7b590,#8fa3b5)"></div>
    <div class="news-date">21 MAY 2018</div>
    <p class="news-text">Lorem Ipsum is simply dummy text of the printing and typesetting industry. Lorem Ipsum has been the industry's standard dummy text ever since the 1500s.</p>
  </article>
  <article class="news-item" style="left:88px;top:269px">
    <div class="news-thumb" role="img" aria-label="Desk with paperwork and laptop" style="background:linear-gradient(135deg,#d9b08c,#f1ece6,#a58a70)"></div>
    <div class="news-date">21 MAY 2018</div>
    <p class="news-text">Lorem Ipsum is simply dummy text of the printing and typesetting industry. Lorem Ipsum has been the industry's standard dummy text ever since the 1500s.</p>
  </article>
  <article class="news-item" style="left:624px;top:269px">
    <div class="news-thumb" role="img" aria-label="Printing press rollers with colour sheets" style="background:linear-gradient(135deg,#1c1e24,#c23a3a,#3a6fc2,#1c1e24)"></div>
    <div class="news-date">21 MAY 2018</div>
    <p class="news-text">Lorem Ipsum is simply dummy text of the printing and typesetting industry. Lorem Ipsum has been the industry's standard dummy text ever since the 1500s.</p>
  </article>
  <div class="btn">VIEW ALL <svg width="10" height="10" viewBox="0 0 10 10"><path d="M1 5h7M5 2l3 3-3 3" stroke="#e0193f" stroke-width="1.8" fill="none"/></svg></div>
</section>

<section class="testimonial" role="region" aria-label="Testimonial over a dark print shop paper roll backdrop">
  <h2 class="section-title">TESTIMONIAL</h2>
  <div class="quote-box">
    <svg width="24" height="20" viewBox="0 0 24 20"><path d="M2 10h7v8H2zM2 10c0-5 2-8 6-9M14 10h7v8h-7zM14 10c0-5 2-8 6-9" fill="#fff" stroke="#fff" stroke-width="1.5"/></svg>
  </div>
  <p class="quote-text">Lorem Ipsum is simply dummy text of the printing and typesetting industry. Lorem Ipsum has been the industry's standard dummy text ever since the 1500s, when an unknown printer took a galley of type and scrambled it to make a type specimen book. It has survived not only five centuries, but also the 1960s with the release of Velmark sheets co.</p>
  <p class="quote-author">JORDAN ELLERY <span>- CEO, FOUNDER</span></p>
  <div class="dots"><span class="dot active"></span><span class="dot"></span></div>
</section>

<section class="contact">
  <h2 class="section-title">CONTACT US</h2>
  <form class="contact-form">
    <div class="customer-q">CURRENT CUSTOMER <span class="radio"><i></i>YES</span><span class="radio"><i class="on"></i>NO</span></div>
    <div class="field-row"><div class="field">Name</div><div class="field">Last Name</div></div>
    <div class="field-row"><div class="field">Email</div><div class="field">Contact No</div></div>
    <div class="field-row"><div class="field">Company Name</div></div>
    <div class="field-row"><div class="field tall">Message</div></div>
  </form>
  <div class="btn">SUBMIT <svg width="10" height="10" viewBox="0 0 10 10"><path d="M1 5h7M5 2l3 3-3 3" stroke="#e0193f" stroke-width="1.8" fill="none"/></svg></div>
</section>

<section class="info">
  <div class="info-item" style="left:131px">
    <svg width="52" height="52" viewBox="0 0 52 52" fill="none" stroke="#2a2d34" stroke-width="2"><rect x="4" y="14" width="44" height="32" rx="2"/><rect x="10" y="4" width="16" height="42"/><rect x="30" y="20" width="12" height="6"/><path d="M30 32h4M38 32h4M30 38h4M38 38h4"/></svg>
    <div><h3>Fax</h3><p>(555) 014-2290</p></div>
  </div>
  <div class="info-item" style="left:471px">
    <svg width="40" height="52" viewBox="0 0 40 52" fill="none" stroke="#2a2d34" stroke-width="2"><rect x="8" y="4" width="24" height="44" rx="3"/><path d="M8 12h24M8 40h24"/></svg>
    <div><h3>Phone</h3><p>(555) 014-7716</p></div>
  </div>
  <div class="info-item" style="left:788px">
    <svg width="50" height="52" viewBox="0 0 50 52" fill="none" stroke="#2a2d34" stroke-width="2"><path d="M25 40C16 28 12 22 12 16a13 13 0 0 1 26 0c0 6-4 12-13 24z"/><circle cx="25" cy="16" r="5"/><path d="M12 36l-8 12h42l-8-12"/></svg>
    <div><h3>Address</h3><p>48 Harrow Works Lane<br>Millbrook, CA 90210-0042</p></div>
  </div>
</section>

<section class="map" role="img" aria-label="Street map showing the office location"></section>

<footer class="site-footer">Tern Hollow ©2018 Privacy Policy Terms | All Right Reserved</footer>

</body>
</html>
```